Bold Vehicle Wrap Design for 2025 Halvorsen Trekmule Cargo Van

We need a full wrap design for our 2025 Halvorsen-Kraft Trekmule 2500 High Roof Cargo Van. This van will be used to represent Brightmark Pro Services, and we want it to stand out with a bold, professional look.

Vehicle Details:
2025 Trekmule 2500
High Roof
144" Wheelbase
Cargo configuration (no windows)

Our current logo is black, white, and gray — but we’re open to more colorful wrap concepts that could even influence a logo recolor.

We want a wrap design that:
Looks bold and professional
Incorporates icons for the services we provide:Plumbing,Handyman, Land Management, Junk and Debris Removal
Incorporates or complements our current logo
Avoids placing critical text or graphics across sliding doors, seams, or complex panel curves
Download all project files (template, logo, reference images):
https://files.quillbarn-share.com/f/7kq2vz9xw4nm18pd5r/BXTLUmQeKsPOtvc3h8rjnZW?key=2pxd9mwq47vbt6c5ls0eyhz3f&s=k8m3vqrt&dl=0

Target Market(s)

ocal residential and commercial customers in need of professional plumbing, handyman, land management, and junk/debris removal services. Homeowners and property managers looking for reliable and skilled service providers. Businesses and contractors who require prompt, professional, and trustworthy support for their facilities and properties. Customers who value quality workmanship and clear branding that conveys professionalism and expertise.

Industry/Entity Type

Local Service Providers specializing in residential and commercial property maintenance

Requirements
Must have
• Incorporate the Brightmark Pro Services logo with flexibility for adding color to complement the wrap. Use bold, professional, and eye-catching colors that stand out on the road. Include icons or visuals representing these key services: Plumbing Handyman Land Management Junk and Debris Removal. Design must fit a 2025 Halvorsen Trekmule 2500 High Roof Cargo Van (144" WB, cargo version with sliding door) — avoid placing important graphics or text over the sliding door seams or complex curves. Use high-contrast text and graphics for maximum readability from a distance. Design should be modern and clean, but bold enough to be memorable. Wrap design must work on all visible sides: driver side, passenger side, rear, and front. Provide final deliverables in Adobe Illustrator (.ai) or Photoshop (.psd) with layered files.
Nice to have
• Mockup images showing the wrap applied to the van template.
Should not have
• Do not place important text, logos, or graphics across the sliding door seam or uneven panel curves — they may get distorted or hidden.No low-contrast text or graphics that make information hard to read from a distance.Do not include any unrelated images or icons that don’t represent Brightmark Pro Services’ core offerings.Do not create a design that looks too similar to competitors or other well-known brands. No fonts that are hard to read or too decorative for a work vehicle.

```html
<!DOCTYPE html>
<html lang="en">
<head>
<meta charset="utf-8">
<title>Brightmark Pro Services – Van Wrap Artwork</title>
<link rel="stylesheet" href="https://fonts.googleapis.com/css2?family=Montserrat:wght@600;700;800;900&family=Oswald:wght@500;600&display=swap">
<style>
  :root {
    --navy: #1d3d6e;
    --navy-deep: #16325c;
    --red: #c8472a;
    --red-soft: #e0653f;
    --white: #ffffff;
    --paper: #ffffff;
    --mascot-green: #6fd13f;
    --mascot-dark: #3f9b2a;
    --text-font: "Montserrat", Arial, sans-serif;
    --condensed-font: "Oswald", "Arial Narrow", sans-serif;
  }
  html, body {
    margin: 0;
    padding: 0;
    width: 1200px;
    height: 2250px;
    overflow: hidden;
    background: var(--paper);
  }
  .canvas {
    position: relative;
    width: 1200px;
    height: 2250px;
  }
  .panel {
    position: absolute;
    display: block;
  }
  .panel--rear-top { left: 120px; top: 140px; width: 430px; height: 602px; }
  .panel--side-top { left: 570px; top: 140px; width: 520px; height: 600px; }
  .panel--side-main { left: 150px; top: 900px; width: 900px; height: 414px; }
  .panel--rear-main { left: 350px; top: 1420px; width: 500px; height: 700px; }

  .brand-name { font-family: var(--text-font); font-weight: 900; fill: var(--navy); }
  .service { font-family: var(--text-font); font-weight: 700; fill: var(--navy); }
  .service--light { fill: var(--white); font-weight: 600; }
  .service--condensed { font-family: var(--condensed-font); font-weight: 500; fill: var(--white); }
  .phone { font-family: var(--text-font); font-weight: 800; fill: var(--white); }
  .phone--condensed { font-family: var(--condensed-font); font-weight: 600; }
  .web { font-family: var(--condensed-font); font-weight: 500; fill: var(--white); }
  .web-accent { fill: var(--red-soft); }
</style>
</head>
<body>
<main class="canvas">

  <!-- Rear doors, upper group -->
  <svg class="panel panel--rear-top" viewBox="0 0 500 700" aria-label="Rear doors wrap">
    <defs>
      <linearGradient id="mascotFillA" x1="0" y1="0" x2="0" y2="1">
        <stop offset="0" stop-color="var(--mascot-green)"/>
        <stop offset="1" stop-color="var(--mascot-dark)"/>
      </linearGradient>
    </defs>
    <rect width="500" height="700" rx="24" fill="var(--white)"/>
    <path class="rear-red-field" d="M0 270 Q0 220 60 215 L190 215 Q250 215 250 280 L250 470 Q380 455 500 425 L500 700 L0 700 Z" fill="var(--red)"/>
    <path class="rear-navy-field" d="M0 560 Q260 545 500 475 L500 700 L0 700 Z" fill="var(--navy)"/>
    <text class="brand-name" x="40" y="92" font-size="50">BRIGHTMARK</text>
    <text class="brand-name" x="40" y="138" font-size="30">PRO SERVICES</text>
    <rect class="mascot" x="30" y="240" width="190" height="250" rx="20" fill="url(#mascotFillA)" role="img" aria-label="Illustration: waving green recycling-bin mascot walking"/>
    <g class="service-list">
      <circle cx="266" cy="242" r="7" fill="var(--red)"/><text class="service" x="280" y="249" font-size="19">PLUMBING</text>
      <circle cx="266" cy="276" r="7" fill="var(--red)"/><text class="service" x="280" y="283" font-size="19">HANDYMAN</text>
      <circle cx="266" cy="310" r="7" fill="var(--red)"/><text class="service" x="280" y="317" font-size="19">LAND MANA</text>
      <text class="service" x="280" y="341" font-size="19">GEMENT</text>
      <circle cx="266" cy="372" r="7" fill="var(--red)"/><text class="service" x="280" y="379" font-size="19">JUNK AND</text>
      <text class="service" x="280" y="403" font-size="19">DEBRIS REMOVAL</text>
    </g>
    <text class="phone" x="250" y="625" font-size="44" text-anchor="middle">(555) 014-2287</text>
    <text class="web" x="470" y="675" font-size="21" text-anchor="end"><tspan class="web-accent">www.</tspan>brightmarkproservices<tspan class="web-accent">.net</tspan></text>
  </svg>

  <!-- Passenger side, upper group -->
  <svg class="panel panel--side-top" viewBox="0 0 520 600" aria-label="Passenger side wrap">
    <defs>
      <linearGradient id="mascotFillB" x1="0" y1="0" x2="0" y2="1">
        <stop offset="0" stop-color="var(--mascot-green)"/>
        <stop offset="1" stop-color="var(--mascot-dark)"/>
      </linearGradient>
    </defs>
    <rect width="520" height="600" rx="20" fill="var(--white)"/>
    <path class="side-red-band" d="M0 250 Q260 180 520 240 L520 600 L0 600 Z" fill="var(--red)"/>
    <path class="side-navy-field" d="M0 290 Q260 220 520 285 L520 600 L0 600 Z" fill="var(--navy)"/>
    <rect class="mascot" x="20" y="30" width="170" height="440" rx="24" fill="url(#mascotFillB)" role="img" aria-label="Illustration: waving green recycling-bin mascot walking"/>
    <text class="brand-name" x="212" y="86" font-size="36">BRIGHTMARK</text>
    <text class="brand-name" x="212" y="120" font-size="22">PRO SERVICES</text>
    <g class="service-list">
      <circle cx="262" cy="324" r="7" fill="var(--red)"/><text class="service--condensed" x="276" y="332" font-size="24">PLUMBING</text>
      <circle cx="262" cy="362" r="7" fill="var(--red)"/><text class="service--condensed" x="276" y="370" font-size="24">HANDYMAN</text>
      <circle cx="262" cy="400" r="7" fill="var(--red)"/><text class="service--condensed" x="276" y="408" font-size="24">LAND MANA</text>
      <text class="service--condensed" x="276" y="436" font-size="24">GEMENT</text>
      <circle cx="262" cy="468" r="7" fill="var(--red)"/><text class="service--condensed" x="276" y="476" font-size="24">JUNK AND</text>
      <text class="service--condensed" x="276" y="504" font-size="24">DEBRIS REMOVAL</text>
    </g>
    <text class="phone phone--condensed" x="20" y="556" font-size="46">(555) 014-2287</text>
  </svg>

  <!-- Driver side, full length -->
  <svg class="panel panel--side-main" viewBox="0 0 1000 460" aria-label="Driver side wrap">
    <defs>
      <linearGradient id="mascotFillC" x1="0" y1="0" x2="0" y2="1">
        <stop offset="0" stop-color="var(--mascot-green)"/>
        <stop offset="1" stop-color="var(--mascot-dark)"/>
      </linearGradient>
    </defs>
    <path class="side-base" d="M20 0 L720 0 Q800 0 860 90 L1000 250 L1000 460 L0 460 L0 20 Q0 0 20 0 Z" fill="var(--white)"/>
    <path class="side-red-band" d="M0 205 Q400 130 760 180 Q880 210 1000 330 L1000 460 L0 460 Z" fill="var(--red)"/>
    <path class="side-navy-field" d="M0 240 Q400 165 740 210 Q860 235 980 360 L1000 460 L0 460 Z" fill="var(--navy)"/>
    <rect class="side-rocker" x="0" y="395" width="1000" height="65" fill="var(--navy-deep)"/>
    <rect class="mascot" x="80" y="10" width="270" height="310" rx="24" fill="url(#mascotFillC)" role="img" aria-label="Illustration: waving green recycling-bin mascot walking"/>
    <text class="brand-name" x="400" y="68" font-size="44">BRIGHTMARK</text>
    <text class="brand-name" x="400" y="104" font-size="26">PRO SERVICES</text>
    <g class="service-list">
      <circle cx="430" cy="215" r="7" fill="var(--red)"/><text class="service service--light" x="446" y="222" font-size="20">PLUMBING</text>
      <circle cx="430" cy="247" r="7" fill="var(--red)"/><text class="service service--light" x="446" y="254" font-size="20">HANDYMAN</text>
      <circle cx="430" cy="279" r="7" fill="var(--red)"/><text class="service service--light" x="446" y="286" font-size="20">LAND MANA</text>
      <text class="service service--light" x="446" y="310" font-size="20">GEMENT</text>
      <circle cx="430" cy="339" r="7" fill="var(--red)"/><text class="service service--light" x="446" y="346" font-size="20">JUNK AND</text>
      <text class="service service--light" x="446" y="370" font-size="20">DEBRIS REMOVAL</text>
    </g>
    <text class="phone" x="40" y="368" font-size="36">(555) 014-2287</text>
    <rect class="web-pill" x="700" y="280" width="240" height="40" rx="8" fill="var(--red)"/>
    <text class="web" x="820" y="307" font-size="17" text-anchor="middle">www.brightmarkproservices.net</text>
  </svg>

  <!-- Rear doors, lower group -->
  <svg class="panel panel--rear-main" viewBox="0 0 500 700" aria-label="Rear doors wrap">
    <defs>
      <linearGradient id="mascotFillD" x1="0" y1="0" x2="0" y2="1">
        <stop offset="0" stop-color="var(--mascot-green)"/>
        <stop offset="1" stop-color="var(--mascot-dark)"/>
      </linearGradient>
    </defs>
    <rect width="500" height="700" rx="24" fill="var(--white)"/>
    <path class="rear-red-field" d="M0 270 Q0 220 60 215 L190 215 Q250 215 250 280 L250 470 Q380 455 500 425 L500 700 L0 700 Z" fill="var(--red)"/>
    <path class="rear-navy-field" d="M0 560 Q260 545 500 475 L500 700 L0 700 Z" fill="var(--navy)"/>
    <text class="brand-name" x="40" y="92" font-size="50">BRIGHTMARK</text>
    <text class="brand-name" x="40" y="138" font-size="30">PRO SERVICES</text>
    <rect class="mascot" x="30" y="240" width="190" height="250" rx="20" fill="url(#mascotFillD)" role="img" aria-label="Illustration: waving green recycling-bin mascot walking"/>
    <g class="service-list">
      <circle cx="266" cy="242" r="7" fill="var(--red)"/><text class="service" x="280" y="249" font-size="19">PLUMBING</text>
      <circle cx="266" cy="276" r="7" fill="var(--red)"/><text class="service" x="280" y="283" font-size="19">HANDYMAN</text>
      <circle cx="266" cy="310" r="7" fill="var(--red)"/><text class="service" x="280" y="317" font-size="19">LAND MANA</text>
      <text class="service" x="280" y="341" font-size="19">GEMENT</text>
      <circle cx="266" cy="372" r="7" fill="var(--red)"/><text class="service" x="280" y="379" font-size="19">JUNK AND</text>
      <text class="service" x="280" y="403" font-size="19">DEBRIS REMOVAL</text>
    </g>
    <text class="phone" x="250" y="625" font-size="44" text-anchor="middle">(555) 014-2287</text>
    <text class="web" x="470" y="675" font-size="21" text-anchor="end"><tspan class="web-accent">www.</tspan>brightmarkproservices<tspan class="web-accent">.net</tspan></text>
  </svg>

</main>
</body>
</html>
```